WWW.VELTRONA.IT BUSINNES CARD

WE NEED A BUSINESS CARD . I HAVE A COMPANY IN ITALY NR 1 IN HAIR MEDICAL CARE AN HAIR REPLECEMENT . IN CARD I NEED WRITE WEB ADDRESS, MAIL , ADDRESS, TELEPHONE NUMBER , AND NAME
IN THE BACK SIDE I NEED MY DOCTOR LOGO .
MY WEB SITE IS WWW.VELTRONA.IT
Updates

Target Market(s)

CONSUMER B2C

Industry/Entity Type

Hair And Beauty

Contact Information for Business Card

I WANT A MEDICAL BUSINESS CARD.

Font styles to use
Other font styles liked:
• VERDANA

Colors
33a6d7
3176b5
85abd2
aedbee
eaf1f7
ffffff

Requirements
Must have
• I NEED MY LOGO AND LOGO OF DR VELTRONA

```html
<!DOCTYPE html>
<html lang="it">
<head>
<meta charset="utf-8">
<title>Veltrona – Biglietto da visita</title>
<link href="https://fonts.googleapis.com/css2?family=Noto+Sans:wght@400;700&family=Questrial&display=swap" rel="stylesheet">
<style>
  :root {
    --navy: #0f2b84;
    --sky: #50a9ce;
    --band-top: #3398c6;
    --band-bottom: #2f74b2;
    --paper: #ffffff;
    --hair-dark: #5a2f1c;
    --hair-light: #a8643e;
  }
  html, body {
    margin: 0;
    padding: 0;
    width: 1200px;
    height: 777px;
    overflow: hidden;
    background: var(--paper);
  }
  .business-card {
    position: relative;
    width: 1200px;
    height: 777px;
    background: var(--paper);
    overflow: hidden;
  }
  .card-art {
    position: absolute;
    inset: 0;
    width: 1200px;
    height: 777px;
  }
  .brand-name {
    font-family: "Noto Sans", Verdana, sans-serif;
    font-weight: 700;
    fill: var(--navy);
  }
  .tagline {
    font-family: "Questrial", "Century Gothic", sans-serif;
    fill: var(--navy);
  }
  .contact-text {
    font-family: "Noto Sans", Verdana, sans-serif;
    fill: var(--paper);
  }
  .contact-icon {
    fill: none;
    stroke: var(--paper);
    stroke-width: 2;
    stroke-linejoin: round;
    stroke-linecap: round;
  }
</style>
</head>
<body>
<main class="business-card">
  <svg class="card-art" viewBox="0 0 1200 777" xmlns="http://www.w3.org/2000/svg">
    <defs>
      <linearGradient id="band-gradient" x1="0" y1="0" x2="0" y2="1">
        <stop offset="0" stop-color="var(--band-top)"/>
        <stop offset="1" stop-color="var(--band-bottom)"/>
      </linearGradient>
      <linearGradient id="mascot-gradient" x1="0" y1="0" x2="0" y2="1">
        <stop offset="0" stop-color="var(--hair-light)"/>
        <stop offset="0.6" stop-color="var(--hair-dark)"/>
        <stop offset="1" stop-color="#e8eef5"/>
      </linearGradient>
    </defs>

    <!-- contact band -->
    <path class="contact-band" d="M0 544 C 380 500, 880 500, 1200 416 L1200 777 L0 777 Z" fill="url(#band-gradient)"/>

    <!-- brand -->
    <g class="brand">
      <rect class="brand-mark" x="96" y="176" width="120" height="120" fill="var(--sky)"/>
      <text class="brand-name" x="352" y="334" font-size="168" textLength="780" lengthAdjust="spacingAndGlyphs">Veltrona</text>
    </g>
    <text class="tagline" x="210" y="412" font-size="44" textLength="776" lengthAdjust="spacingAndGlyphs">CURA E REINTEGRAZIONE DEI CAPELLI</text>

    <!-- mascot area -->
    <rect class="mascot" role="img" aria-label="Mascotte illustrata: un capello sorridente in camice da medico" x="84" y="380" width="116" height="350" rx="40" fill="url(#mascot-gradient)"/>

    <!-- contacts -->
    <g class="contact-list">
      <path class="contact-icon icon-phone" d="M744 520 c-8 4 -10 12 -6 22 c8 18 20 30 38 38 c10 4 18 2 22 -6 l-10 -10 c-4 -3 -8 -2 -10 1 l-3 4 c-10 -5 -18 -13 -23 -23 l4 -3 c3 -2 4 -6 1 -10 Z"/>
      <text class="contact-text" x="818" y="564" font-size="44" textLength="308" lengthAdjust="spacingAndGlyphs">+39045318274</text>

      <g class="contact-icon icon-mail">
        <rect x="736" y="585" width="46" height="30"/>
        <path d="M736 585 L759 603 L782 585 M736 615 L753 600 M782 615 L765 600"/>
      </g>
      <text class="contact-text" x="830" y="620" font-size="44" textLength="292" lengthAdjust="spacingAndGlyphs">info@veltrona.it</text>

      <g class="contact-icon icon-web">
        <circle cx="759" cy="657" r="21"/>
        <ellipse cx="759" cy="657" rx="9" ry="21"/>
        <path d="M738 657 H780 M741 646 H777 M741 668 H777 M759 636 V678"/>
      </g>
      <text class="contact-text" x="830" y="675" font-size="44" textLength="300" lengthAdjust="spacingAndGlyphs">www.veltrona.it</text>

      <g class="contact-icon icon-pin">
        <path d="M375 732 C 362 716, 360 708, 360 703 a15 15 0 0 1 30 0 c0 5 -2 13 -15 29 Z"/>
        <circle cx="375" cy="703" r="5"/>
      </g>
      <text class="contact-text" x="422" y="727" font-size="44" textLength="698" lengthAdjust="spacingAndGlyphs">Dirección Via Lucerna 14 Verona Itay</text>
    </g>
  </svg>
</main>
</body>
</html>
```